PEACFUL ACUPUNCTURE PRACTITIONER NEEDS A NEW COAT

I need a new design for an exiting website http://willowgateneedlework.com/ for a acupuncturist. This will be a minimalism design with lots and lots of white space. Home page and one interior page. Please keep the feeling of calm and peaceful serenity. For Color scheme: https://www.morningfernclinic.com/fertility. The bottom part of the home page with sections and links to the service pages: https://harborlotuswellness.com/. The client likes this the best: http://mfclinic.com/. I'm attaching the logo and content pages.

Target Market(s)

Women

Industry/Entity Type

Wellness, health, wellbeing, meditation

Number of Pages Required

2 page

Font styles to use
Sans Serif
Decorative

Colors

Designer to choose colors to be used in the design.

Requirements
Must have
Nice to have
• Follow new website drafts and links
Should not have
• Busy with bright colors. No poping

```html
<!DOCTYPE html>
<html lang="en">
<head>
<meta charset="utf-8">
<title>Willowgate – Website Design</title>
<link rel="stylesheet" href="https://fonts.googleapis.com/css2?family=Josefin+Sans:wght@300;400;600;700&display=swap">
<style>
:root{
  --board:#f5ebed;
  --mauve:#b48a90;
  --mauve-dark:#8f666c;
  --rose-light:#e6d3d6;
  --ink:#6e5357;
  --muted:#9c8589;
  --white:#ffffff;
  --soft:#f7f2f3;
  --line:#eadfe1;
}
*{box-sizing:border-box;margin:0;padding:0}
html,body{width:1200px;height:2556px;overflow:hidden}
body{background:var(--board);font-family:"Josefin Sans",sans-serif;color:var(--ink);position:relative}

.board-head{position:absolute;top:118px;left:262px;width:700px;height:70px;display:flex;align-items:center;gap:70px}
.brand{display:flex;align-items:center;gap:10px}
.brand-dot{width:26px;height:26px;border-radius:50%;background:var(--mauve)}
.brand-name{font-size:20px;font-weight:400;color:var(--mauve-dark);line-height:1}
.brand-name small{display:block;font-size:8px;letter-spacing:2px;margin-top:3px}
.spec h4{font-size:14px;font-weight:600;color:var(--ink);margin-bottom:6px}
.spec p{font-size:11px;color:var(--muted);line-height:1.3}
.swatches{display:flex;gap:8px}
.swatch{width:26px;height:26px;border-radius:50%}
.swatch-label{font-size:7px;color:var(--muted);text-align:center;margin-top:3px}

.side-label{position:absolute;font-size:12px;letter-spacing:5px;color:var(--muted);writing-mode:vertical-rl;transform:rotate(180deg)}
.label-desktop{left:78px;top:1440px}
.label-mobile{left:1130px;top:1600px}

/* desktop page */
.page{position:absolute;background:var(--white);overflow:hidden}
.desktop{left:160px;top:848px;width:768px;height:1612px}
.topbar{height:12px;background:var(--mauve)}
.site-head{height:44px;display:flex;align-items:center;justify-content:center;gap:8px}
.site-head .brand-dot{width:18px;height:18px}
.site-head .brand-name{font-size:14px}
.nav{display:flex;justify-content:center;gap:22px;font-size:8px;color:var(--muted);padding:6px 0 10px;border-bottom:1px solid var(--line)}
.hero{position:relative;height:330px;background:linear-gradient(100deg,#f8f1f1 0%,#efdcd8 45%,#d9b9b0 75%,#c9a69c 100%)}
.hero-text{position:absolute;left:56px;top:95px;width:280px}
.hero h1{font-size:26px;font-weight:700;line-height:1.1;color:var(--mauve-dark);letter-spacing:.5px}
.hero p{font-size:9px;line-height:1.5;color:var(--ink);margin:12px 0 16px}
.btn{display:inline-block;background:var(--mauve);color:var(--white);font-size:8px;padding:7px 14px;border-radius:14px;letter-spacing:.5px}

.section{padding:40px 80px;text-align:center}
.section h2{font-size:22px;font-weight:400;color:var(--mauve-dark);margin-bottom:14px}
.section p{font-size:8.5px;line-height:1.7;color:var(--muted)}
.about{background:var(--soft);display:flex;align-items:center;gap:50px;text-align:left;padding:50px 80px}
.about-copy{flex:1}
.about-photo{width:160px;height:160px;border-radius:50%;background:radial-gradient(circle at 50% 40%,#e7b79d,#c78468 60%,#b7968f);flex:none;border:6px solid var(--white)}
.focus-grid{display:flex;justify-content:center;gap:16px;margin-top:20px}
.focus-card{width:132px;height:150px;background:var(--soft);border:1px solid var(--line);display:flex;flex-direction:column;align-items:center;justify-content:center;gap:14px;font-size:9px;color:var(--ink)}
.schedule{border-top:1px solid var(--line)}
.footer{position:absolute;bottom:0;left:0;right:0;height:40px;background:var(--rose-light);font-size:7px;color:var(--ink);display:flex;align-items:center;justify-content:center}

/* mobile page */
.mobile{left:968px;top:848px;width:120px;height:1612px}
.mobile .topbar{height:6px}
.mobile .site-head{height:30px;gap:4px}
.mobile .site-head .brand-dot{width:10px;height:10px}
.mobile .site-head .brand-name{font-size:8px}
.m-hero{height:150px;background:linear-gradient(160deg,#f8f1f1 0%,#ecd6d1 55%,#d3b1a7 100%);padding:30px 10px}
.m-hero h1{font-size:10px;font-weight:700;color:var(--mauve-dark);line-height:1.15}
.m-hero .btn{font-size:5px;padding:4px 8px;margin-top:8px}
.m-sec{padding:16px 10px}
.m-sec h2{font-size:8px;font-weight:400;color:var(--mauve-dark);margin-bottom:6px}
.m-sec p{font-size:4.5px;line-height:1.6;color:var(--muted)}
.m-soft{background:var(--soft)}
.m-photo{width:62px;height:62px;border-radius:50%;background:radial-gradient(circle at 50% 40%,#e7b79d,#c78468 60%,#b7968f);margin:10px 0}
.m-card{height:62px;background:var(--soft);border:1px solid var(--line);margin-top:8px;display:flex;align-items:center;justify-content:center;font-size:5px}
.mobile .footer{height:24px;font-size:4px}
</style>
</head>
<body>

<header class="board-head">
  <div class="brand"><div class="brand-dot"></div><div class="brand-name">Willowgate<small>ACUPUNCTURE</small></div></div>
  <div class="spec"><h4>Fonts:</h4><p>Josefin<br>Sans</p></div>
  <div class="spec"><h4>Colors:</h4>
    <div class="swatches">
      <div><div class="swatch" style="background:var(--mauve)"></div><div class="swatch-label">B48A90</div></div>
      <div><div class="swatch" style="background:var(--rose-light)"></div><div class="swatch-label">E6D3D6</div></div>
      <div><div class="swatch" style="background:var(--white)"></div><div class="swatch-label">FFFFFF</div></div>
    </div>
  </div>
</header>

<div class="side-label label-desktop">LAPTOP | DESKTOP</div>
<div class="side-label label-mobile">MOBILE</div>

<main class="page desktop">
  <div class="topbar"></div>
  <div class="site-head"><div class="brand-dot"></div><div class="brand-name">Willowgate</div></div>
  <nav class="nav"><span>Home</span><span>About</span><span>Women's Health</span><span>Services</span><span>Fertility</span><span>Pain Relief</span><span>Emotional Wellbeing</span><span>Book Now</span><span>Contact</span></nav>
  <section class="hero" role="img" aria-label="Photo of a calm acupuncture treatment in soft light">
    <div class="hero-text">
      <h1>WELCOME TO<br>WILLOWGATE</h1>
      <p>Gentle, personal care for women at every stage of life. We blend traditional acupuncture with a quiet, restful space so you can slow down, breathe and heal.</p>
      <span class="btn">LEARN MORE</span>
    </div>
  </section>
  <section class="section">
    <h2>Philosophy of Care</h2>
    <p>At Willowgate we believe healing begins when the body and mind are given room to rest. Each visit is unhurried and shaped around you, your history and your goals. We listen first, then treat gently, supporting your natural balance with care that feels warm, safe and deeply calming.</p>
    <p style="margin-top:10px">Our practice welcomes women seeking relief from stress, pain, hormonal change and fertility concerns, offering steady support through every season of life.</p>
  </section>
  <section class="about">
    <div class="about-copy">
      <h2 style="font-size:22px;font-weight:400;color:var(--mauve-dark);margin-bottom:14px">About Mara</h2>
      <p style="font-size:8.5px;line-height:1.7;color:var(--muted)">Mara is a licensed acupuncturist with many years of quiet, focused practice in women's health. She trained in classical methods and continues to study herbal care and gentle bodywork. Her patients describe her as calm, attentive and kind. She treats each person as a whole, caring for body, mind and spirit together, and helps each woman feel heard and at ease.</p>
      <div style="margin-top:18px"><span class="btn">READ MORE</span></div>
    </div>
    <div class="about-photo" role="img" aria-label="Portrait photo of the acupuncturist"></div>
  </section>
  <section class="section">
    <h2>Areas of Focus</h2>
    <div class="focus-grid">
      <div class="focus-card"><svg width="30" height="30" viewBox="0 0 30 30" fill="none" stroke="#b48a90" stroke-width="1.5"><circle cx="15" cy="15" r="11"/><path d="M9 15h12M15 9v12"/></svg>Women's Health</div>
      <div class="focus-card"><svg width="30" height="30" viewBox="0 0 30 30" fill="none" stroke="#b48a90" stroke-width="1.5"><circle cx="15" cy="15" r="11"/><circle cx="15" cy="15" r="4"/></svg>Fertility</div>
      <div class="focus-card"><svg width="30" height="30" viewBox="0 0 30 30" fill="none" stroke="#b48a90" stroke-width="1.5"><path d="M6 20l9-12 9 12z"/></svg>Pain Relief</div>
      <div class="focus-card"><svg width="30" height="30" viewBox="0 0 30 30" fill="none" stroke="#b48a90" stroke-width="1.5"><path d="M15 24s-9-6-9-12a5 5 0 0 1 9-2 5 5 0 0 1 9 2c0 6-9 12-9 12z"/></svg>Emotional Wellbeing</div>
    </div>
  </section>
  <section class="section schedule">
    <h2>Schedule a Free 20-Minute Consultation</h2>
    <p>Not sure if acupuncture is right for you? Book a short, free call to talk through your needs and ask any questions.</p>
    <div style="margin-top:18px"><span class="btn">BOOK NOW</span></div>
  </section>
  <footer class="footer">© Willowgate Acupuncture · All rights reserved</footer>
</main>

<main class="page mobile">
  <div class="topbar"></div>
  <div class="site-head"><div class="brand-dot"></div><div class="brand-name">Willowgate</div></div>
  <section class="m-hero" role="img" aria-label="Photo of a calm acupuncture treatment">
    <h1>WELCOME TO<br>WILLOWGATE</h1>
    <span class="btn">LEARN MORE</span>
  </section>
  <section class="m-sec">
    <h2>Philosophy of Care</h2>
    <p>At Willowgate we believe healing begins when body and mind are given room to rest. Each visit is unhurried and shaped around you, supporting your natural balance with calm care.</p>
  </section>
  <section class="m-sec m-soft">
    <h2>About Mara</h2>
    <div class="m-photo" role="img" aria-label="Portrait photo of the acupuncturist"></div>
    <p>Mara is a licensed acupuncturist focused on women's health, known for her calm, attentive and kind approach to whole-person care.</p>
  </section>
  <section class="m-sec">
    <h2>Areas of Focus</h2>
    <div class="m-card">Women's Health</div>
    <div class="m-card">Fertility</div>
    <div class="m-card">Pain Relief</div>
    <div class="m-card">Emotional Wellbeing</div>
  </section>
  <section class="m-sec m-soft">
    <h2>Schedule a Free 20-Minute Consultation</h2>
    <p>Book a short, free call to talk through your needs.</p>
    <span class="btn" style="font-size:5px;padding:4px 8px;margin-top:6px">BOOK NOW</span>
  </section>
  <footer class="footer">© Willowgate Acupuncture</footer>
</main>

</body>
</html>
```